The Lumo-Hub for Rescue Drills + Crowd Care Post Card

Hi! I am a new business that is Licensed Training Provider to the National Bluefield Aid. We teach private CPR/AED, First Aid and a variety of other emergency training courses to the general public! Our goal is to get into businesses of all sizes from the mom and pops store to corporate offices of Manhattan. We can do private classes in your home and no office space is to small! We even have a school assembly program that teaches "Hands Only CPR" for children. I'm looking to make a post card to hand out that can easily explain what we are doing…that might have some good visuals that catch your eye as well. I def want to use The Lumo Hub logo in it that I have attached. Im not necessarily married to any of the other images. You can check out our website www.lumohubdrills.example for more information and you can use any of the images on there as well if you would like. I will give you free reign to find any cool photo stock image that you might think fits with what I'm trying to do. Hopefully you can help!
Updates

Also feel free to use any other photos that you might find that you think fit our cause for teaching CPR/First aid etc!! Thanks!

Thank you all for your hard work. I actually like many of these designs and really torn! I will be making some decisions in the next day or so. Thank you! Wendel

Industry/Entity Type

Training

```html
<!DOCTYPE html>
<html lang="en">
<head>
<meta charset="utf-8">
<title>The Lumo Hub – Postcard</title>
<link href="https://fonts.googleapis.com/css2?family=Oswald:wght@500;700&family=Open+Sans:ital,wght@0,600;0,700;1,700&family=Raleway:wght@300&display=swap" rel="stylesheet">
<style>
  :root {
    --bg: #e9dcc4;
    --black: #111111;
    --red: #e0201f;
    --blue: #1d6fc0;
    --white: #ffffff;
    --grey-dark: #3a3a3a;
    --grey-mid: #4c4c4c;
    --cream: #fffdf6;
  }
  * { margin: 0; padding: 0; box-sizing: border-box; }
  html, body { width: 1200px; height: 500px; overflow: hidden; }
  body { background: var(--bg); font-family: "Open Sans", sans-serif; position: relative; }

  .card { position: absolute; top: 33px; height: 433px; overflow: hidden; }

  /* Front side */
  .card--front { left: 28px; width: 560px; background: var(--black); }
  .front-header { position: absolute; left: 0; top: 0; width: 560px; height: 108px; }
  .brand-logo {
    position: absolute; left: 24px; top: 14px;
    font-family: "Raleway", sans-serif; font-weight: 300;
    font-size: 62px; letter-spacing: 1px; color: var(--white); white-space: nowrap;
    display: flex; align-items: center; gap: 12px;
  }
  .brand-logo .brand-mark { width: 30px; height: 30px; background: var(--red); display: inline-block; }
  .tagline {
    position: absolute; right: 4px; top: 88px;
    font-family: "Open Sans", sans-serif; font-weight: 700; font-size: 13px;
    color: var(--red); letter-spacing: 0.3px;
  }
  .front-body {
    position: absolute; left: 0; top: 108px; width: 560px; height: 205px;
    background: var(--cream); border-left: 7px solid var(--red); border-right: 4px solid var(--red);
  }
  .photo-child {
    position: absolute; left: 0; top: 0; width: 203px; height: 205px;
    background: linear-gradient(160deg, #f4ede4 0%, #e8cdb4 55%, #d9b597 100%);
  }
  .badge {
    position: absolute; left: 220px; top: 10px; width: 96px; height: 62px;
  }
  .badge-text { font-size: 7.5px; font-weight: 700; color: var(--black); text-align: right; width: 70px; line-height: 1.2; }
  .badge-text .save { color: var(--red); }
  .headline-block { position: absolute; left: 320px; top: 6px; width: 236px; text-align: center; }
  .headline-learn { font-family: "Open Sans", sans-serif; font-weight: 700; font-size: 19px; color: var(--blue); line-height: 1.1; }
  .headline-learn span { color: var(--red); }
  .headline-main {
    font-family: "Oswald", sans-serif; font-weight: 700; font-size: 46px; color: var(--blue);
    line-height: 1; transform: scaleX(0.9);
  }
  .headline-sub { position: absolute; left: 220px; top: 88px; width: 330px; font-size: 12.5px; font-weight: 700; color: var(--blue); line-height: 1.25; text-align: center; }
  .headline-ped { position: absolute; left: 220px; top: 119px; width: 330px; text-align: center; font-family: "Oswald", sans-serif; font-weight: 700; font-size: 16px; color: var(--red); }
  .intro { position: absolute; left: 218px; top: 147px; width: 335px; font-size: 11px; font-weight: 600; color: var(--black); line-height: 1.35; }

  .front-footer { position: absolute; left: 0; top: 313px; width: 560px; height: 120px; border-left: 7px solid var(--red); border-right: 4px solid var(--red); border-bottom: 4px solid var(--red); }
  .why { position: absolute; left: 6px; top: 2px; width: 262px; color: var(--white); }
  .why h3 { font-size: 13.5px; font-weight: 700; color: var(--red); }
  .why p { font-size: 11px; font-weight: 600; line-height: 1.25; margin-top: 2px; }
  .why p.note { font-style: italic; font-weight: 700; margin-top: 4px; }
  .schedule { position: absolute; left: 292px; top: 23px; width: 262px; text-align: center; color: var(--white); font-weight: 700; }
  .schedule .ask { font-size: 12.5px; line-height: 1.25; }
  .schedule .phone { font-size: 19px; color: var(--red); margin-top: 6px; line-height: 1.1; }
  .schedule .visit { font-size: 13px; line-height: 1.3; }
  .schedule .web { font-size: 13.5px; margin-top: 2px; }

  /* Back side */
  .card--back { left: 610px; width: 560px; background: radial-gradient(ellipse at 30% 35%, var(--grey-mid) 0%, var(--grey-dark) 70%); }
  .photo-family {
    position: absolute; left: 15px; top: 27px; width: 250px; height: 250px; border-radius: 50%;
    border: 3px solid var(--red);
    background: linear-gradient(150deg, #d7c6b0 0%, #c99f7f 45%, #8c6b55 100%);
  }
  .back-copy { position: absolute; left: 282px; top: 62px; width: 270px; color: var(--white); }
  .back-copy h2 { font-family: "Open Sans", sans-serif; font-weight: 700; font-size: 17px; line-height: 1.2; }
  .back-copy h2 span { color: var(--red); }
  .back-copy p { font-size: 12px; font-weight: 600; line-height: 1.35; margin-top: 12px; }
  .back-cta { position: absolute; left: 130px; top: 293px; width: 300px; text-align: center; }
  .cta-line { font-family: "Oswald", sans-serif; font-weight: 700; font-size: 19px; color: var(--white); line-height: 1.1; }
  .cta-act { font-family: "Oswald", sans-serif; font-weight: 700; font-size: 23px; color: var(--red); letter-spacing: 1.5px; line-height: 1.15; }
  .back-logo {
    margin: 4px auto 0; width: 280px; height: 52px; background: var(--black);
    display: flex; align-items: center; justify-content: center; gap: 8px;
    font-family: "Raleway", sans-serif; font-weight: 300; font-size: 32px; color: var(--white); white-space: nowrap;
  }
  .back-logo .brand-mark { width: 16px; height: 16px; background: var(--red); }
  .back-call { margin-top: 3px; font-family: "Open Sans", sans-serif; font-weight: 700; font-size: 17px; color: var(--white); letter-spacing: 2px; white-space: nowrap; }
</style>
</head>
<body>

<section class="card card--front">
  <header class="front-header">
    <div class="brand-logo">The Lumo Hub <span class="brand-mark"></span></div>
    <div class="tagline">RESCUE DRILLS + CROWD CARE</div>
  </header>

  <div class="front-body">
    <div class="photo-child" role="img" aria-label="Photo of a smiling baby holding a small Learn CPR sign"></div>

    <div class="badge">
      <div class="badge-text">Get CPR trained.<br><span class="save">Save a life.</span></div>
      <svg width="96" height="44" viewBox="0 0 96 44" aria-label="Partner badge">
        <circle cx="22" cy="24" r="18" fill="#d8d8d8"/>
        <rect x="52" y="16" width="16" height="16" fill="var(--red)"/>
        <rect x="72" y="20" width="22" height="8" fill="#bbbbbb"/>
      </svg>
    </div>

    <div class="headline-block">
      <div class="headline-learn">Learn <span>FIRST AID</span></div>
      <div class="headline-main">CPR &amp; AED</div>
    </div>
    <div class="headline-sub">Cardiopulmonary Resuscitation &amp;<br>Automated External Defibrillator</div>
    <div class="headline-ped">Pediatric First Aid CPR AED</div>
    <p class="intro">We are a Licensed Training Provider to the National Bluefield Aid. We can do private classes in your home or office. We even have a school assembly program that teaches "Hands Only CPR" for children.</p>
  </div>

  <footer class="front-footer">
    <div class="why">
      <h3>Why should you be trained?</h3>
      <p>Acting appropriately when dealing with everyday hazards such as choking, allergic reactions or even falls in the playground can save a life.</p>
      <p class="note">You never know when you may be faced with a life or death situation.</p>
    </div>
    <div class="schedule">
      <div class="ask">TO SCHEDULE A HOME, OFFICE OR<br>SCHOOL CPR/FIRST AID CLASS,</div>
      <div class="phone">CALL 555.010.4477</div>
      <div class="visit">Or Visit Us at</div>
      <div class="web">www.lumohubdrills.example</div>
    </div>
  </footer>
</section>

<section class="card card--back">
  <div class="photo-family" role="img" aria-label="Circular photo of a laughing family with two young children"></div>
  <div class="back-copy">
    <h2>Take a <span>big step</span> to protect your little ones</h2>
    <p>Our Pediatric First Aid and CPR courses are accessible, affordable and attainable for everyone. Designed to provide members of the public with the knowledge and techniques that are needed to properly perform CPR and First Aid in any unforeseen emergency, our training is an invaluable resource.</p>
  </div>
  <div class="back-cta">
    <div class="cta-line">LEARN CPR, BE A LIFE SAVER!</div>
    <div class="cta-act">KNOW HOW TO ACT</div>
    <div class="back-logo">The Lumo Hub <span class="brand-mark"></span></div>
    <div class="back-call">CALL US: 555.010.4477</div>
  </div>
</section>

</body>
</html>
```